business card design for luxurious real estate brand

using the attached logo, i am looking for a 2-sided business card design. the back should be the gold logo on black background. the front needs to include: gold logo, name, phone, email, and website

Industry/Entity Type

real estate

Contact Information for Business Card

logo, name, email, phone, website

Font styles to use
Sans Serif

```html
<!DOCTYPE html>
<html lang="en">
<head>
<meta charset="utf-8">
<title>Casa Verano – Business Card</title>
<link rel="stylesheet" href="https://fonts.googleapis.com/css2?family=Montserrat:wght@400;500&family=Open+Sans:wght@700&display=swap">
<style>
  :root {
    --backdrop: #c6c6c6;
    --card: #1a1a1a;
    --pattern-light: #2f2f2f;
    --pattern-mid: #1c1c1c;
    --pattern-dark: #0a0a0a;
    --pattern-ink: #353535;
    --gold: #fccb0b;
    --ink-light: #f2f2f2;
  }
  * { margin: 0; padding: 0; box-sizing: border-box; }
  html, body {
    width: 1200px;
    height: 896px;
    overflow: hidden;
    background: var(--backdrop);
  }
  .canvas {
    position: relative;
    width: 1200px;
    height: 896px;
  }
  .card {
    position: absolute;
    left: 334px;
    width: 528px;
    height: 301px;
    border-radius: 30px;
    background: var(--card);
    overflow: hidden;
  }
  .card--back { top: 125px; }
  .card--front { top: 475px; }

  /* Back: tone-on-tone surface with the brand name as the mark */
  .card__pattern {
    position: absolute;
    inset: 0;
    background: linear-gradient(120deg, var(--pattern-light) 0%, var(--pattern-mid) 50%, var(--pattern-dark) 100%);
  }
  .card__pattern-name {
    position: absolute;
    inset: 0;
    display: flex;
    align-items: center;
    justify-content: center;
    font-family: "Montserrat", sans-serif;
    font-weight: 500;
    font-size: 30px;
    letter-spacing: 9px;
    color: var(--pattern-ink);
    white-space: nowrap;
  }

  /* Front */
  .brand {
    position: absolute;
    left: 56px;
    top: 178px;
    width: 228px;
    text-align: center;
    font-family: "Montserrat", sans-serif;
    font-weight: 500;
    font-size: 21px;
    line-height: 30px;
    letter-spacing: 6.5px;
    color: var(--gold);
    white-space: nowrap;
  }

  .divider {
    position: absolute;
    left: 297px;
    top: 91px;
    width: 2px;
    height: 119px;
    background: var(--gold);
  }

  .contact {
    position: absolute;
    left: 312px;
    top: 82px;
  }
  .contact__name {
    font-family: "Open Sans", sans-serif;
    font-weight: 700;
    font-size: 23px;
    line-height: 1.2;
    color: var(--gold);
    white-space: nowrap;
  }
  .contact__role {
    font-family: "Montserrat", sans-serif;
    font-weight: 400;
    font-size: 14px;
    line-height: 1.2;
    color: var(--ink-light);
    margin-top: 1px;
  }
  .contact__list {
    list-style: none;
    margin-top: 24px;
  }
  .contact__item {
    display: flex;
    align-items: center;
    gap: 5px;
    font-family: "Montserrat", sans-serif;
    font-size: 13px;
    color: var(--ink-light);
    height: 20.5px;
    white-space: nowrap;
  }
  .contact__icon {
    width: 12px;
    height: 12px;
    fill: var(--gold);
    flex: none;
  }
</style>
</head>
<body>
<main class="canvas">

  <section class="card card--back" aria-label="Card back">
    <div class="card__pattern" role="img" aria-label="Tone-on-tone repeating brand pattern fading from grey to black"></div>
    <div class="card__pattern-name">CASA VERANO</div>
  </section>

  <section class="card card--front" aria-label="Card front">
    <div class="brand">CASA VERANO</div>

    <div class="divider"></div>

    <div class="contact">
      <h1 class="contact__name">MARTIN HALE</h1>
      <p class="contact__role">Managing Director</p>
      <ul class="contact__list">
        <li class="contact__item">
          <svg class="contact__icon" viewBox="0 0 24 24" aria-hidden="true"><path d="M6.6 10.8a15.1 15.1 0 0 0 6.6 6.6l2.2-2.2a1 1 0 0 1 1-.25 11.4 11.4 0 0 0 3.6.57 1 1 0 0 1 1 1V20a1 1 0 0 1-1 1A17 17 0 0 1 3 4a1 1 0 0 1 1-1h3.5a1 1 0 0 1 1 1c0 1.25.2 2.450.57 3.57a1 1 0 0 1-.25 1z"/></svg>
          123 456 789
        </li>
        <li class="contact__item">
          <svg class="contact__icon" viewBox="0 0 24 24" aria-hidden="true"><path d="M2 5h20v2l-10 6L2 7z M2 9l10 6 10-6v10H2z"/></svg>
          info@yourgmail.com
        </li>
        <li class="contact__item">
          <svg class="contact__icon" viewBox="0 0 24 24" aria-hidden="true"><path d="M12 2a10 10 0 1 0 0 20 10 10 0 0 0 0-20zm0 2c1 0 2.3 2 2.8 5H9.2C9.7 6 11 4 12 4zM4.3 11h4.6a20 20 0 0 0 0 2H4.3a8 8 0 0 1 0-2zm6.6 0h2.2a18 18 0 0 1 0 2h-2.2a18 18 0 0 1 0-2zm4.2 0h4.6a8 8 0 0 1 0 2h-4.6a20 20 0 0 0 0-2zM9.2 15h5.6c-.5 3-1.8 5-2.8 5s-2.3-2-2.8-5z"/></svg>
          www.yourwebsite.com
        </li>
      </ul>
    </div>
  </section>

</main>
</body>
</html>
```